Boat business cards

I'm looking for business cards with the two logos I've attached. I don't have an specific idea in mind and open to anything. All the usual info will be on the card. Name, position in company, nr, email, address, ect. The company rents out these two boats for charters and fishing.

```html
<!DOCTYPE html>
<html lang="en">
<head>
<meta charset="utf-8">
<title>Silver Tide Charters – Business Cards</title>
<link href="https://fonts.googleapis.com/css2?family=Montserrat:wght@400;500&display=swap" rel="stylesheet">
<style>
  :root {
    --backdrop: #8a8a8c;
    --card: #0b0b0c;
    --card-edge: #5b86d4;
    --accent-blue: #5b8ee0;
    --text-light: #f2f2f2;
    --hull-brown: #8a6a45;
    --deck-white: #e9e9e9;
    --sky-blue: #8fb2e6;
  }
  * { box-sizing: border-box; margin: 0; padding: 0; }
  html, body { width: 1200px; height: 800px; overflow: hidden; }
  body {
    background: var(--backdrop);
    font-family: "Montserrat", sans-serif;
    display: flex;
    align-items: center;
    justify-content: center;
    gap: 48px;
  }
  .card {
    width: 532px;
    height: 304px;
    background: var(--card);
    border-bottom: 2px solid var(--card-edge);
    border-right: 2px solid var(--card-edge);
    position: relative;
    overflow: hidden;
  }
  /* Contact side */
  .contact {
    position: absolute;
    left: 34px;
    top: 44px;
    color: var(--text-light);
  }
  .contact__name {
    color: var(--accent-blue);
    font-size: 22px;
    font-weight: 400;
    letter-spacing: 0.5px;
  }
  .contact__role {
    color: var(--accent-blue);
    font-size: 13px;
    display: flex;
    align-items: center;
    gap: 8px;
    margin: 2px 0 16px;
  }
  .contact__role::before {
    content: "";
    width: 40px;
    height: 1px;
    background: var(--accent-blue);
  }
  .contact__line {
    font-size: 12.5px;
    line-height: 1.75;
  }
  .contact__boat {
    position: absolute;
    right: 0;
    bottom: 0;
    width: 300px;
    height: 120px;
    background: linear-gradient(170deg, var(--deck-white) 0%, var(--deck-white) 40%, var(--hull-brown) 41%, var(--hull-brown) 85%, var(--accent-blue) 86%);
    clip-path: polygon(0 100%, 100% 0, 100% 100%);
  }
  /* Brand side */
  .brand {
    display: flex;
    flex-direction: column;
    align-items: center;
    justify-content: center;
    gap: 8px;
    height: 100%;
  }
  .brand__boat--sport {
    width: 170px;
    height: 52px;
    background: linear-gradient(180deg, var(--deck-white), var(--sky-blue));
    border-radius: 4px 24px 4px 4px;
  }
  .brand__boat--yacht {
    width: 150px;
    height: 36px;
    background: linear-gradient(180deg, var(--deck-white) 0%, var(--hull-brown) 55%, var(--accent-blue) 100%);
    border-radius: 2px 18px 2px 2px;
  }
  .brand__name {
    color: var(--text-light);
    font-size: 22px;
    font-weight: 500;
    letter-spacing: 2px;
    text-transform: uppercase;
  }
  .brand__name--secondary {
    font-size: 18px;
    margin-bottom: 6px;
  }
</style>
</head>
<body>
  <section class="card card--contact">
    <div class="contact">
      <h1 class="contact__name">DANIEL HARPER</h1>
      <p class="contact__role">President</p>
      <p class="contact__line">214 Harbor View Road, Juneau, Alaska 99801</p>
      <p class="contact__line">555-014-2738 | daniel@silvertide.com</p>
      <p class="contact__line">www.silvertide.com</p>
    </div>
    <div class="contact__boat" role="img" aria-label="Side-view illustration of a motor yacht with white superstructure and brown hull over blue water lines"></div>
  </section>

  <section class="card card--brand">
    <div class="brand">
      <div class="brand__boat--sport" role="img" aria-label="Illustration of a blue sport-fishing boat"></div>
      <p class="brand__name brand__name--secondary">Sea Breeze</p>
      <div class="brand__boat--yacht" role="img" aria-label="Small illustration of a motor yacht with brown hull"></div>
      <p class="brand__name">Silver Tide</p>
    </div>
  </section>
</body>
</html>
```